New Word Template Design Project

I want design about template plant date palm tree
The size is A4/Users/mibu/Desktop/DSC07540.JPG
/Users/mibu/Desktop/DSC07514.JPG

```html
<!DOCTYPE html>
<html lang="en">
<head>
<meta charset="utf-8">
<title>Date Palm Letterhead Template</title>
<link rel="stylesheet" href="https://fonts.googleapis.com/css2?family=Didact+Gothic&display=swap">
<style>
  :root {
    --paper: #f0efeb;
    --ink: #262626;
    --frond-dark: #2f5443;
    --frond-olive: #7d8a4c;
    --frond-sage: #93a397;
    --frond-straw: #b3b27a;
    --frond-pale: #e8e2a4;
    --ground: #eeede8;
  }
  * { margin: 0; padding: 0; box-sizing: border-box; }
  html, body {
    width: 848px;
    height: 1200px;
    overflow: hidden;
    background: var(--ground);
  }
  .letterhead {
    position: relative;
    width: 848px;
    height: 1200px;
    overflow: hidden;
    font-family: "Didact Gothic", "Century Gothic", sans-serif;
    color: var(--ink);
  }
  .palm-border {
    position: absolute;
    inset: 0;
    background:
      radial-gradient(ellipse at 10% 15%, var(--frond-dark) 0%, transparent 45%),
      radial-gradient(ellipse at 90% 10%, var(--frond-straw) 0%, transparent 45%),
      radial-gradient(ellipse at 5% 60%, var(--frond-olive) 0%, transparent 45%),
      radial-gradient(ellipse at 95% 55%, var(--frond-sage) 0%, transparent 45%),
      radial-gradient(ellipse at 20% 95%, var(--frond-dark) 0%, transparent 45%),
      radial-gradient(ellipse at 85% 95%, var(--frond-olive) 0%, transparent 45%),
      linear-gradient(135deg, var(--frond-sage), var(--frond-straw) 50%, var(--frond-sage));
  }
  .sheet {
    position: absolute;
    left: 111px;
    top: 99px;
    width: 626px;
    height: 1001px;
    background: var(--paper);
  }
  .logo-box {
    position: absolute;
    left: 199px;
    top: 57px;
    width: 228px;
    height: 107px;
    border: 1px solid var(--ink);
    display: flex;
    align-items: center;
    justify-content: center;
    font-size: 15px;
    letter-spacing: 0.3px;
  }
  .letter-body {
    position: absolute;
    left: 74px;
    top: 226px;
    width: 486px;
    font-size: 13.6px;
    line-height: 17.1px;
  }
  .letter-body p + p { margin-top: 17.1px; }
</style>
</head>
<body>
<main class="letterhead">
  <div class="palm-border" role="img" aria-label="Illustrated border of overlapping date palm fronds in dark green, olive, sage and pale yellow"></div>
  <section class="sheet">
    <div class="logo-box">LOGO</div>
    <article class="letter-body">
      <p>Quis nostrud exercitation</p>
      <p>Ut enim ad minima veniam, quis nostrum exercitationem ullam corpo-<br>ris suscipit laboriosam, nisi ut aliquid ex.</p>
      <p>Ut enim ad minima veniam, quis nostrum exercitationem ullam corpo-<br>ris suscipit laboriosam, nisi ut aliquid ex ea commodi consequatur?<br>Quis autem vel eum iure reprehenderit qui in vel illum qui dolorem<br>eum fugiat quo voluptas nulla pariatur.</p>
      <p>Lorem ipsum dolor sit amet, consectetur adipiscing elit, sed do<br>eiusmod tempor incididunt ut labore et dolore magna aliqua. Ut enim<br>ad minim veniam, quis nostrud exercitation ullamco laboris nisi ut<br>aliquip ex ea commodo consequat. Duis aute irure dolor in reprehen-<br>derit in voluptate velit esse cillum dolore eu fugiat nulla pariatur.<br>Excepteur sint occaecat cupidatat non proident, sunt in culpa qui<br>officia deserunt mollit anim id est laborum.</p>
      <p>Sed ut perspiciatis unde omnis iste natus error sit voluptatem accusan-<br>tium doloremque laudantium, totam rem aperiam, eaque ipsa quae<br>ab illo inventore veritatis et quasi architecto beatae vitae dicta sunt<br>explicabo. Nemo enim ipsam voluptatem quia voluptas sit aspernatur<br>aut odit aut fugit.</p>
      <p>Sed quia consequuntur magni dolores eos qui ratione voluptatem<br>sequi nesciunt. Neque porro quisquam est, qui dolorem ipsum quia<br>dolor sit amet. Consectetur, adipisci velit, sed quia non numquam eius<br>modi tempora inl eum iure reprehenderit qui in ea voluptate velit esse<br>quam nihil molestiae consequatur, vel illum qui dolorem eum fugiat<br>quo voluptas nulla pariatur?<br>&nbsp;reprehenderit qui in ea voluptate velit esse quam nihil molestiae<br>consequatur, vel illum qui dolorem eum fugiat quo voluptas nulla<br>olorem eum fugiat quo voluptas nulla pariatur?<br>oluptas nulla pariatur?</p>
      <p>Corporis suscipit laboriosam, nisi ut aliquid ex ea commodi consequa-<br>tur? Quis autem vel eum iure reprehenderit qui in ea voluptate velit<br>esse quam nihil molestiae consequatur, vel illum qui dolorem eum<br>fugiat quo voluptas nulla pariatur?</p>
      <p>Quis nostrud</p>
    </article>
  </section>
</main>
</body>
</html>
```